Business Card Design

we are a brand new cable TV network devoted to self improvement and leading a better life called FLOURIVO TV.I have a logo. We have 3 executives that need cards.I want it to be a heavy stock card: professional but showing our creative nature

Industry/Entity Type

Business

Contact Information for Business Card

CLAUDIA SAENZ AMLIECEO350 San Juan DrPonte Vedra Beach FL 32082904-473-5953

```html
<!DOCTYPE html>
<html lang="en">
<head>
<meta charset="utf-8">
<title>Flourivo TV — Business Card</title>
<link rel="stylesheet" href="https://fonts.googleapis.com/css2?family=Jost:wght@400;500;600&display=swap">
<style>
  :root {
    --backdrop: #d8cec3;
    --card: #0c0c0d;
    --silver: #d9d5d0;
    --accent-red: #8e2b2b;
    --text-warm: #c9b9aa;
    --rule-start: #b7a594;
    --disc: #bdb8b2;
  }
  html, body {
    margin: 0;
    padding: 0;
    width: 1200px;
    height: 970px;
    overflow: hidden;
    background: var(--backdrop);
  }
  .canvas {
    position: relative;
    width: 1200px;
    height: 970px;
  }
  .business-card {
    position: absolute;
    left: 150px;
    top: 235px;
    width: 900px;
    height: 500px;
    border-radius: 28px;
    background: var(--card);
    box-shadow: 0 18px 40px rgba(0, 0, 0, 0.25);
    overflow: hidden;
    font-family: "Jost", sans-serif;
  }
  .brand-name {
    position: absolute;
    left: 43px;
    top: 64px;
    margin: 0;
    font-size: 66px;
    font-weight: 600;
    letter-spacing: 1px;
    color: var(--silver);
    line-height: 1;
    white-space: nowrap;
  }
  .person-name {
    position: absolute;
    left: 43px;
    top: 247px;
    margin: 0;
    font-size: 27px;
    font-weight: 600;
    color: var(--accent-red);
    line-height: 1;
    white-space: nowrap;
  }
  .person-title {
    position: absolute;
    left: 43px;
    top: 289px;
    display: flex;
    align-items: center;
    gap: 10px;
    font-size: 21px;
    font-weight: 400;
    letter-spacing: 1px;
    color: var(--text-warm);
    line-height: 1;
  }
  .title-rule {
    width: 316px;
    height: 2px;
    background: linear-gradient(to right, var(--rule-start), rgba(183, 165, 148, 0));
  }
  .contact-list {
    position: absolute;
    left: 43px;
    top: 360px;
    margin: 0;
    padding: 0;
    list-style: none;
    font-size: 23px;
    font-weight: 400;
    letter-spacing: 0.6px;
    color: var(--text-warm);
  }
  .contact-item {
    display: flex;
    align-items: flex-start;
    gap: 10px;
    line-height: 30px;
    white-space: nowrap;
  }
  .contact-item + .contact-item {
    margin-top: 15px;
  }
  .contact-icon {
    width: 22px;
    height: 22px;
    margin-top: 4px;
    flex: none;
  }
  .contact-address {
    font-style: normal;
  }
  .brand-disc {
    position: absolute;
    left: 543px;
    top: 173px;
    width: 280px;
    height: 280px;
    border-radius: 50%;
    background: var(--disc);
  }
</style>
</head>
<body>
  <main class="canvas">
    <section class="business-card" aria-label="Flourivo TV business card">
      <h1 class="brand-name">FLOURIVO TV</h1>

      <h2 class="person-name">Mirella Okafor Dunst</h2>
      <div class="person-title">
        <span>CEO</span>
        <span class="title-rule"></span>
      </div>

      <ul class="contact-list">
        <li class="contact-item">
          <svg class="contact-icon" viewBox="0 0 24 24" aria-hidden="true">
            <path d="M6.6 10.8a15.2 15.2 0 0 0 6.6 6.6l2.2-2.2c.3-.3.7-.4 1-.2 1.1.4 2.3.6 3.6.6.6 0 1 .4 1 1V20c0 .6-.4 1-1 1A17 17 0 0 1 3 4c0-.6.4-1 1-1h3.5c.6 0 1 .4 1 1 0 1.3.2 2.5.6 3.6.1.3 0 .7-.2 1z" fill="var(--accent-red)"/>
            <path d="M14 3.5a7 7 0 0 1 6.5 6.5M14 7a3.5 3.5 0 0 1 3 3" stroke="var(--accent-red)" stroke-width="1.8" fill="none" stroke-linecap="round"/>
          </svg>
          <span>555-618-2047</span>
        </li>
        <li class="contact-item">
          <svg class="contact-icon" viewBox="0 0 24 24" aria-hidden="true">
            <path d="M12 2a7 7 0 0 0-7 7c0 5.2 7 13 7 13s7-7.8 7-13a7 7 0 0 0-7-7zm0 9.5A2.5 2.5 0 1 1 12 6.5a2.5 2.5 0 0 1 0 5z" fill="var(--accent-red)"/>
          </svg>
          <address class="contact-address">718 Harlow Creek Dr<br>Corley Sands FL 34219</address>
        </li>
      </ul>

      <div class="brand-disc" aria-hidden="true"></div>
    </section>
  </main>
</body>
</html>
```